Business price tag design for Furniture Business

Hello,

I have developed a tag for a home furniture business and need 1 more creative template. Please see attachment. I need the template to be very appealing.

Requirements:

1.Tag dimensions needs to be about the same as attached tag.
2. Tag design needs to be suitable for a home furniture business.
3. Tag needs to have locations for the following: Item Title, Now Price, Was Price, Product Number.
4. "The black shape at the bottom of attached tag could be removed.

I have no requirements on colors, but something professional is needed, preferably white background to reduce print ink consumption.

Please see attachment for clarification.

Industry/Entity Type

Retail

Font styles to use
Serif
Sans Serif

Requirements
Must have
• Please see Project Description.
Nice to have

```html
<!DOCTYPE html>
<html lang="en">
<head>
<meta charset="utf-8">
<title>Corvane Furniture Outlet – Price Tag</title>
<link rel="stylesheet" href="https://fonts.googleapis.com/css2?family=Arimo:wght@400&display=swap">
<style>
  :root {
    --tag-green: #7dc242;
    --tag-brown: #8b5a3c;
    --tag-paper: #ffffff;
  }
  html, body {
    margin: 0;
    padding: 0;
    width: 1200px;
    height: 2308px;
    overflow: hidden;
    background: var(--tag-paper);
  }
  .price-tag {
    display: block;
    width: 1200px;
    height: 2308px;
    font-family: "Arimo", Arial, sans-serif;
  }
  .outer-frame { fill: none; stroke: var(--tag-green); stroke-width: 3; }
  .inner-frame { fill: none; stroke: var(--tag-brown); stroke-width: 1; }
  .panel { fill: var(--tag-paper); stroke: var(--tag-green); stroke-width: 1.3; }
  .label { fill: var(--tag-green); }
  .value { fill: var(--tag-brown); }
  .store-name { font-size: 24px; }
  .label-small { font-size: 15px; }
  .label-tiny { font-size: 13px; }
  .label-medium { font-size: 20px; }
  .item-title { font-size: 20px; }
  .product-number { font-size: 15px; }
  .now-price { font-size: 44px; }
  .was-price { font-size: 27px; }
</style>
</head>
<body>
<svg class="price-tag" viewBox="0 0 300 577" preserveAspectRatio="none" xmlns="http://www.w3.org/2000/svg">
  <rect class="outer-frame" x="3" y="3" width="294" height="571"/>
  <rect class="inner-frame" x="14" y="12" width="273" height="552" rx="22" ry="22"/>

  <g class="store-block">
    <path class="panel" d="M107,15 H258 V93.7 A60,60 0 0 0 212,153 H107 Z"/>
    <text class="label store-name" x="128" y="55">Corvane</text>
    <text class="label store-name" x="128" y="87">Furniture</text>
    <text class="label store-name" x="128" y="119">Outlet</text>
  </g>

  <g class="title-block">
    <path class="panel" d="M107,160 H212.5 A60,60 0 0 0 258,210 V280 H107 Z"/>
    <text class="label label-small" x="135" y="187">Item Title</text>
    <text class="value item-title" x="134" y="222">Black</text>
    <text class="value item-title" x="134" y="251">King Bed</text>
  </g>

  <g class="product-block">
    <rect class="panel" x="107" y="288" width="151" height="55"/>
    <text class="label label-tiny" x="133" y="309">Product Number</text>
    <text class="value product-number" x="133" y="331">B9999</text>
  </g>

  <g class="now-price-block">
    <path class="panel" d="M107,350 H258 V470 H133 A56,56 0 0 0 107,420 Z"/>
    <text class="label label-medium" x="134" y="377">Now Price</text>
    <text class="value now-price" x="132" y="440">$555</text>
  </g>

  <g class="was-price-block">
    <path class="panel" d="M133,478 H258 V557 H107 V515 A57,57 0 0 0 133,478 Z"/>
    <text class="label label-medium" x="136" y="502">Was Price</text>
    <text class="value was-price" x="134" y="540">$666</text>
  </g>
</svg>
</body>
</html>
```